Design a menu for health restaurant

A health food restaurant in Los Angeles is seeking menu design. Our foods are made from scratch using whole ingredients.
Name: Grubb Larder
Address: 1000 E 60th StLos Angeles, CA 90247
Website: www.GrubbLarder.example
We are looking for a clean and simple menu. Brand colors are white/tan, green and orange.

Please see attached excel with menu items and logo. We do not yet have prices.

Colors
f78f20
9bcb3c
ffffff
fff3d1

Requirements
Must have
• Easy to read.
Trifold menu design (front and back).
VEGAN, VEGETARIAN, GLUTEN FREE, CONTAINS NUTS symbols.
Logo.
Nice to have
• Incorporate brand colors, but still be easy to read.
We would like to use the Belco font (attached) if it works. If not we are open to a similar font that is easy to read.

Please see attached images.
We like the images and headers of OPTION 1. Would like something similar in trifold format.
We like the clean fonts of OPTION 2.

```html
<!DOCTYPE html>
<html lang="en">
<head>
<meta charset="utf-8">
<title>Grubb Larder — Menu</title>
<link rel="stylesheet" href="https://fonts.googleapis.com/css2?family=Montserrat:wght@400;500;600&display=swap">
<style>
:root{
  --orange:#f78f20;
  --green:#9bcb3c;
  --tan:#fff3d1;
  --white:#ffffff;
  --ink:#111111;
  --photo-warm:#d9a04a;
  --photo-green:#6f9a3e;
  --photo-berry:#8e4f97;
}
*{box-sizing:border-box;margin:0;padding:0}
html,body{width:1200px;height:934px;overflow:hidden;background:var(--white)}
body{position:relative;font-family:"Montserrat",Arial,sans-serif;color:var(--ink)}
.abs{position:absolute}
.band{position:absolute;height:21px;font-size:17.5px;font-weight:500;line-height:21px;letter-spacing:.2px}
.band--orange{background:var(--orange)}
.band--green{background:var(--green)}
.band--tan{background:var(--tan)}
.legend{position:absolute;top:34px;left:100px;display:flex}
.legend__item{width:61px;display:flex;flex-direction:column;align-items:center;font-size:5.3px;line-height:5.5px;text-align:center}
.legend__item svg{width:24px;height:17px;margin-bottom:2px}
.item{position:absolute;width:341px}
.item__head{display:flex;align-items:center;height:18px}
.item__name{font-size:12px;font-weight:600;letter-spacing:.1px;white-space:nowrap}
.item__price{margin-left:auto;font-size:12px;font-weight:600}
.item__note{font-size:12px;margin-left:4px}
.item p{font-size:12px;line-height:12.6px;margin-top:4px}
.icon{width:17px;height:17px;margin-left:7px;flex:none}
.icon--nut{width:24px}
.stack{position:absolute;width:160px}
.stack .item__name{white-space:normal;line-height:12.6px}
.stack .icons{display:flex;align-items:center;height:20px}
.stack .icons .icon{margin-left:0;margin-right:6px}
.stack p{font-size:12px;line-height:12.6px}
.stack .item__price{display:block;margin-left:0}
.photo{position:absolute}
</style>
</head>
<body>

<svg width="0" height="0" style="position:absolute" aria-hidden="true">
  <defs>
    <symbol id="i-vegan" viewBox="0 0 24 18">
      <path d="M3 16 C7 9 12 6 21 3" fill="none" stroke="#111" stroke-width="1.4"/>
      <path d="M10 12 C9 6 14 2 22 1 C21 8 17 12 10 12Z" fill="#111"/>
      <path d="M8 13 C3 12 1 8 2 4 C6 5 9 8 8 13Z" fill="#111"/>
    </symbol>
    <symbol id="i-veg" viewBox="0 0 24 18">
      <path d="M5 17 C8 10 13 6 21 3" fill="none" stroke="#111" stroke-width="1.4"/>
      <path d="M11 11 C10 5 15 2 22 1 C21 7 17 11 11 11Z" fill="#111"/>
      <path d="M9 12 C4 11 2 7 3 3 C7 4 10 7 9 12Z" fill="none" stroke="#111" stroke-width="1.3"/>
    </symbol>
    <symbol id="i-gf" viewBox="0 0 20 20">
      <circle cx="10" cy="10" r="8.6" fill="none" stroke="#111" stroke-width="1.4"/>
      <path d="M10 4 V16" stroke="#111" stroke-width="1.3"/>
      <g fill="#111">
        <ellipse cx="8.2" cy="7" rx="1.4" ry="2" transform="rotate(-30 8.2 7)"/>
        <ellipse cx="11.8" cy="7" rx="1.4" ry="2" transform="rotate(30 11.8 7)"/>
        <ellipse cx="8.2" cy="10.2" rx="1.4" ry="2" transform="rotate(-30 8.2 10.2)"/>
        <ellipse cx="11.8" cy="10.2" rx="1.4" ry="2" transform="rotate(30 11.8 10.2)"/>
        <ellipse cx="10" cy="4.3" rx="1.1" ry="1.8"/>
      </g>
    </symbol>
    <symbol id="i-nut" viewBox="0 0 28 14">
      <ellipse cx="7" cy="7" rx="6.5" ry="5.5" fill="#111"/>
      <ellipse cx="21" cy="7" rx="6.5" ry="5.5" fill="#111"/>
      <rect x="7" y="3.5" width="14" height="7" fill="#111"/>
    </symbol>
  </defs>
</svg>

<!-- Legend -->
<div class="legend">
  <div class="legend__item"><svg><use href="#i-vegan"/></svg>VEGAN</div>
  <div class="legend__item"><svg><use href="#i-veg"/></svg>VEGETARIAN</div>
  <div class="legend__item"><svg viewBox="0 0 20 20"><use href="#i-gf"/></svg>GLUTEN<br>FREE</div>
  <div class="legend__item"><svg viewBox="0 0 28 14"><use href="#i-nut"/></svg>CONTAINS<br>NUTS</div>
</div>

<!-- Breakfast -->
<div class="band band--orange" style="left:13px;top:96px;width:280px;padding-left:27px">BREAKFAST</div>

<div class="item" style="left:40px;top:138px">
  <div class="item__head"><span class="item__name">PASTRIES</span><svg class="icon"><use href="#i-veg"/></svg><span class="item__price">$11.99</span></div>
  <p>Croissant (regular, almond, chocolate)<br>Blueberry Muffin<br>Superseed Cookie</p>
</div>
<div class="item" style="left:40px;top:211px">
  <div class="item__head"><span class="item__name">PARFAIT</span><svg class="icon"><use href="#i-veg"/></svg><span class="item__price">$11.99</span></div>
  <p>Fresh strawberries and blueberries on yogurt and muesli and topped with honey drizzle.</p>
</div>
<div class="item" style="left:40px;top:271px">
  <div class="item__head"><span class="item__name">AVOCADO SUPER TOAST</span><svg class="icon"><use href="#i-vegan"/></svg><span class="item__price">$11.99</span></div>
  <p>Avocado Mash, Tomato, Basil, Ground Flax, Hemp Seed, Chickpeas, and Moringa Powder on Whole Wheat Bread.</p>
</div>
<div class="item" style="left:40px;top:336px">
  <div class="item__head"><span class="item__name">BRUNCH BURGER</span><span class="item__price">$11.99</span></div>
  <p>House seasoned beef burger topped with an over medium egg, red leaf lettuce, tomato, housemade pickles and Larder Sauce on a bun.</p>
</div>
<div class="item" style="left:40px;top:414px">
  <div class="item__head"><span class="item__name">BREAKFAST SAMMY</span><svg class="icon"><use href="#i-vegan"/></svg><span class="item__note">option</span><span class="item__price">$11.99</span></div>
  <p>Your choice of over medium egg or tofu steak with guacamole, tomato, and Larder sauce on an English muffin.</p>
</div>
<div class="item" style="left:40px;top:488px">
  <div class="item__head"><span class="item__name">AM BURRITO</span><svg class="icon"><use href="#i-veg"/></svg><span class="item__price">$11.99</span></div>
  <p>Scrambled eggs, onion, red bell pepper, black beans, housemade salsa, yogurt, and pepper jack cheese in a tortilla.</p>
</div>

<!-- Smoothies -->
<div class="band band--tan" style="left:13px;top:593px;width:279px;padding-left:26px">SMOOTHIES</div>

<div class="stack" style="left:39px;top:636px">
  <div class="item__name">GREEN MACHINE<br>SMOOTHIE</div>
  <div class="icons" style="margin-top:5px"><svg class="icon"><use href="#i-vegan"/></svg><svg class="icon" viewBox="0 0 20 20"><use href="#i-gf"/></svg><svg class="icon icon--nut" viewBox="0 0 28 14"><use href="#i-nut"/></svg></div>
  <p style="margin-top:7px">Romaine, spinach, banana, mango, pineapple, flaxmilk, spirulina, almond butter</p>
  <span class="item__price" style="margin-top:16px">$11.99</span>
</div>
<div class="stack" style="left:220px;top:636px;width:175px">
  <div class="item__name">ACAI SMOOTHIE</div>
  <div class="icons" style="margin-top:18px"><svg class="icon"><use href="#i-vegan"/></svg><svg class="icon" viewBox="0 0 20 20"><use href="#i-gf"/></svg><svg class="icon icon--nut" viewBox="0 0 28 14"><use href="#i-nut"/></svg></div>
  <p style="margin-top:7px">Acai, blueberries, banana, pineapple, Macqui berry, flaxmilk, almond butter</p>
  <span class="item__price" style="margin-top:16px">$11.99</span>
</div>
<div class="stack" style="left:39px;top:793px">
  <div class="item__name">MANGO SMOOTHIE</div>
  <div class="icons" style="margin-top:15px"><svg class="icon"><use href="#i-vegan"/></svg><svg class="icon" viewBox="0 0 20 20"><use href="#i-gf"/></svg></div>
  <p style="margin-top:10px">Mango, flaxmilk, banan,<br>hemp seeds</p>
  <span class="item__price" style="margin-top:10px">$11.99</span>
</div>

<svg class="photo" style="left:193px;top:725px" width="219" height="207" role="img" aria-label="Photo of a purple berry smoothie in a glass">
  <defs>
    <linearGradient id="g-smoothie" x1="0" y1="0" x2="1" y2="1">
      <stop offset="0" stop-color="#eeeeef"/>
      <stop offset=".5" stop-color="var(--photo-berry)"/>
      <stop offset="1" stop-color="#e4e4e6"/>
    </linearGradient>
  </defs>
  <polygon points="0,108 219,0 219,207" fill="url(#g-smoothie)"/>
</svg>

<!-- Bowls -->
<div class="band band--green" style="left:412px;top:28px;width:292px;padding-left:39px">BOWLS</div>

<div class="item" style="left:451px;top:71px">
  <div class="item__head"><span class="item__name">SOUTHWEST BOWL</span><svg class="icon" viewBox="0 0 20 20"><use href="#i-gf"/></svg><svg class="icon icon--nut" viewBox="0 0 28 14" style="margin-left:5px"><use href="#i-nut"/></svg><span class="item__price">$11.99</span></div>
  <p>Your choice of protein with corn, black beans, red onions, almonds and avocado over quinoa with lime hot sauce.</p>
</div>
<div class="item" style="left:451px;top:135px">
  <div class="item__head"><span class="item__name">CHIMI BOWL</span><svg class="icon" viewBox="0 0 20 20"><use href="#i-gf"/></svg><span class="item__price">$11.99</span></div>
  <p>Your choice of protein with red bell pepper, mushrooms, zucchini, squash, onion, cherry tomatoes and fresh herb chimichurri on wild and brown rice.</p>
</div>
<div class="item" style="left:451px;top:212px">
  <div class="item__head"><span class="item__name">SOBA NOODLE BOWL</span><span class="item__price">$11.99</span></div>
  <p>Your choice of protein with spinach, snow peas, roasted carrots, red bell pepper, cilantro, sesame seeds and ginger lime sauce over soba noodles.</p>
</div>
<div class="item" style="left:451px;top:291px">
  <div class="item__head"><span class="item__name">HOLLYWOOD BOWL</span><svg class="icon" viewBox="0 0 20 20"><use href="#i-gf"/></svg><span class="item__price">$11.99</span></div>
  <p>Your choice of protein with broccoli, roasted corn, cherry tomatoes, basil, pepitas, flax seeds and lemon juice on wild and brown rice.</p>
</div>
<div class="item" style="left:451px;top:367px">
  <div class="item__head"><span class="item__name">LARDER BOWL</span><svg class="icon" viewBox="0 0 20 20"><use href="#i-gf"/></svg><span class="item__price">$11.99</span></div>
  <p>Your choice of protein with roasted chickpeas and cauliflower, zesty fennel salad and citrus yogurt.</p>
</div>
<div class="item" style="left:451px;top:430px">
  <div class="item__head"><span class="item__name">BUDDHA BOWL</span><span class="item__price">$11.99</span></div>
  <p>Your choice of protein with corn, red kale, sweet potatoes, red cabbage, parsley, oregano, hummus, and farro.</p>
</div>
<div class="item" style="left:451px;top:502px">
  <div class="item__head"><span class="item__name">CHILI RICE BOWL</span><svg class="icon" viewBox="0 0 20 20"><use href="#i-gf"/></svg><span class="item__price">$11.99</span></div>
  <p>Chicken, onions, bell peppers, jalapeños, black &amp; kidney beans, and tomato over brown rice.</p>
</div>

<svg class="photo" style="left:412px;top:568px" width="397" height="111" role="img" aria-label="Photo of a bowl with greens, golden beets, olives, tomatoes and a scoop of hummus">
  <defs>
    <radialGradient id="g-bowl" cx=".5" cy=".55" r=".7">
      <stop offset="0" stop-color="#efe0c4"/>
      <stop offset=".35" stop-color="var(--photo-warm)"/>
      <stop offset=".7" stop-color="var(--photo-green)"/>
      <stop offset="1" stop-color="#e9e9e6"/>
    </radialGradient>
  </defs>
  <rect width="397" height="111" fill="url(#g-bowl)"/>
</svg>

<!-- Soups -->
<div class="band band--orange" style="left:412px;top:693px;width:292px;padding-left:39px">SOUPS</div>

<div class="item" style="left:451px;top:733px">
  <div class="item__head"><span class="item__name">CHICKEN NOODLE</span><svg class="icon" viewBox="0 0 20 20"><use href="#i-gf"/></svg><span class="item__price">$11.99</span></div>
  <p>Chicken, egg noodles, root vegetables, oregano &amp; peppercorns.</p>
</div>
<div class="item" style="left:451px;top:796px">
  <div class="item__head"><span class="item__name">LARDER CHILI</span><svg class="icon" viewBox="0 0 20 20"><use href="#i-gf"/></svg><span class="item__price">$11.99</span></div>
  <p>Chicken, onions, bell peppers, jalapeños, black &amp; kidney beans, and tomato.</p>
</div>
<div class="item" style="left:451px;top:861px">
  <div class="item__head"><span class="item__name">SEASONAL ROTATING</span><svg class="icon"><use href="#i-vegan"/></svg><svg class="icon" viewBox="0 0 20 20"><use href="#i-gf"/></svg><span class="item__price">$11.99</span></div>
  <p>(Butternut Squash Soup V+, GF) Butternut squash blended with warm spices, and coconut milk.</p>
</div>

<!-- Wraps -->
<div class="band band--tan" style="left:809px;top:28px;width:292px;padding-left:21px">WRAPS</div>

<div class="item" style="left:830px;top:71px">
  <div class="item__head"><span class="item__name">RANCHER'S WRAP</span><span class="item__price">$11.99</span></div>
  <p>Tomato, red onion, hard boiled egg, avocado, feta cheese, microgreens, romaine, grilled chicken and Ranch dressing in a grilled wrap.</p>
</div>
<div class="item" style="left:830px;top:145px">
  <div class="item__head"><span class="item__name">VEGAN TUNA WRAP</span><svg class="icon"><use href="#i-vegan"/></svg><span class="item__price">$11.99</span></div>
  <p>Vegan tuna, romaine, avocado, celery, shallot, and oregano with Herbalicious Sauce in a whole grain wrap.</p>
</div>
<div class="item" style="left:828px;top:211px">
  <div class="item__head"><span class="item__name" style="padding-left:2px">VEGETARIAN WRAP</span><svg class="icon"><use href="#i-veg"/></svg><span class="item__price">$11.99</span></div>
  <p>Roasted chickpeas, romaine, avocado, red bell pepper, shaved carrots, cucumber, spinach, basil, black beans and feta with lemon-hummus in a sprouted 7-grain wrap.</p>
</div>

<!-- Salad -->
<div class="band band--green" style="left:809px;top:315px;width:292px;padding-left:21px">SALAD</div>

<div class="stack" style="left:829px;top:358px">
  <div class="item__name">AVOCADO, GOLDEN<br>BEET, AND<br>CRANBERRY SALAD</div>
  <div class="icons" style="margin-top:5px"><svg class="icon"><use href="#i-veg"/></svg><svg class="icon" viewBox="0 0 20 20"><use href="#i-gf"/></svg></div>
  <p style="margin-top:10px">Gold beets, avocado, dried cranberries, watermelon radish, red kale, romaine, mixed greens, and pepitas served with Golden Buddha dressing.</p>
</div>
<div class="stack" style="left:1014px;top:358px">
  <div class="item__name">BURRATA SALAD</div>
  <div class="icons" style="margin-top:30px"><svg class="icon"><use href="#i-veg"/></svg><svg class="icon" viewBox="0 0 20 20"><use href="#i-gf"/></svg></div>
  <p style="margin-top:10px">Tomato, melon, shredded basil, balsamic glaze, fresh cracked pepper, and olive oil with burrata.</p>
  <span class="item__price" style="margin-top:12px">$11.99</span>
</div>
<div class="stack" style="left:830px;top:552px">
  <div class="item__name">MEDITERRANEAN<br>SALAD</div>
  <div class="icons" style="margin-top:5px;padding-left:25px"><svg class="icon" viewBox="0 0 20 20"><use href="#i-gf"/></svg></div>
  <p style="margin-top:10px">Cucumbers, Kalamata olives, cherry tomatoes, parsley, tricolor quinoa, hard-boiled egg, and hummus on mixed greens, romaine, and red cabbage with lemon-olive oil dressing.</p>
</div>
<div class="stack" style="left:1015px;top:552px">
  <div class="item__name">VEGAN CHEF SALAD</div>
  <div class="icons" style="margin-top:18px"><svg class="icon"><use href="#i-vegan"/></svg><svg class="icon" viewBox="0 0 20 20"><use href="#i-gf"/></svg><svg class="icon icon--nut" viewBox="0 0 28 14"><use href="#i-nut"/></svg></div>
  <p style="margin-top:10px">Roasted potatoes and carrots, chickpeas, avocado, microgreens and walnuts on mixed greens, romaine, and red kale with vegan ranch.</p>
  <span class="item__price" style="margin-top:11px">$11.99</span>
</div>
<div class="stack" style="left:1015px;top:755px">
  <div class="item__name">RANCHER'S SALAD</div>
  <div class="icons" style="margin-top:18px"><svg class="icon"><use href="#i-veg"/></svg><svg class="icon" viewBox="0 0 20 20"><use href="#i-gf"/></svg></div>
  <p style="margin-top:10px">Tomato, red onion, hard boiled egg, avocado, feta cheese, microgreens, and grilled chicken on romaine with Ranch dressing.</p>
  <span class="item__price" style="margin-top:12px">$11.99</span>
</div>

<svg class="photo" style="left:809px;top:742px" width="200" height="190" role="img" aria-label="Photo of a salad with greens, watermelon radish, avocado and golden beets">
  <defs>
    <linearGradient id="g-salad" x1="0" y1="0" x2="1" y2="1">
      <stop offset="0" stop-color="#e6e6e3"/>
      <stop offset=".45" stop-color="var(--photo-green)"/>
      <stop offset=".7" stop-color="#c9687f"/>
      <stop offset="1" stop-color="#dedcd6"/>
    </linearGradient>
  </defs>
  <polygon points="0,0 199,93 0,190" fill="url(#g-salad)"/>
</svg>

</body>
</html>
```